Website design for an edge protection barrier system

- The design must be based around the attached HPID (home page information design) called CODE HPID. I've attached Word and PDF versions - these are the same. The table boxes are just for approximate placement of information – you DON'T have to make it look exactly like this. All fonts used in the HPID are only examples - you can use any Google font you wish.

- Information only is in orange text. Copy to go on the design in black text. Some instructions are in the HPID. Please be creative!

- The design needs to be modern. Colours are to be black and white with orange ...like the logo colours.

- I've provided the images for the galleries - they are labelled and will match the name in the HPID.

- Examples of some websites that have great design... don't copy them please but they are similar in look to what we are after....
http://wandertrail.co.nz/
http://www.lumfuel.co.nz/
http://www.tolbertwade.co.nz/

Width of content will be 1100 pixels when implemented as a web page. Header height (without nav bar) 150-160 pixels.

If your design is chosen the winning PSD file will have to be provided as follows…
1. Canvas size of 2000px x 2000px - 72ppi in Adobe Photoshop (CS5 compatible)
2. Width of content section is 1100px wide - centered in the canvas
3. Any button rollovers/hovers in the PSD as hidden layers.
4. All fonts used must be Google fonts (except for the fonts in the header at the top of the page).
5. You will need to supply the chosen home page plus one example page (example page as a style guide for how all other pages will look). Example page is only the header and navigational bar at the top, an empty sector in the middle with a column (180 px wide) which can be left or right aligned which means the main sector is 920 pixels wide, and then the footer at the bottom of the page
Updates

Hi all, As per the HPID for the main image gallery you must use: File 7: edge protection systems for new houses hp wednesday, 17 december 2014 04:35:4112 AND File 9: K Bracket for new home edge protection hp wednesday, 17 december 2014 04:35:4111 Use these images so they fit next to each other with the words: Edge protection systems for new houses with timber or aluminium rails (These words must be used either on or above or below the gallery) What we are looking for is a clean modern layout of the home page. The images supplied must be used please. Thank you.

Our office is closed over the New Year holiday season so decisions on designs may be delayed.

```html
<!DOCTYPE html>
<html lang="en">
<head>
<meta charset="utf-8">
<title>Kerbline Safety – Edge Protection Systems</title>
<link href="https://fonts.googleapis.com/css2?family=Raleway:wght@400;500;600;700&display=swap" rel="stylesheet">
<style>
:root{
  --ink:#1a1512;
  --orange:#f5a51d;
  --orange-deep:#e8920c;
  --white:#ffffff;
  --text:#222;
  --grey:#e6e6e6;
}
*{box-sizing:border-box;margin:0;padding:0}
html,body{width:1200px;height:3361px;overflow:hidden}
body{font-family:'Raleway',sans-serif;color:var(--text);background:var(--white);position:relative}
.abs{position:absolute}

/* header */
.site-header{left:0;top:0;width:1200px;height:135px;background:var(--ink)}
.brand{left:125px;top:36px;display:flex;align-items:center;gap:12px;color:var(--orange);font-size:34px;font-weight:600}
.brand-dot{width:26px;height:26px;border-radius:50%;background:var(--orange)}
.tagline{right:124px;top:38px;color:var(--orange);font-size:13px}
.phone{right:124px;top:70px;display:flex;align-items:center;gap:14px;color:var(--orange);font-size:15px;font-weight:600}
.phone-icon{width:26px;height:26px;background:var(--orange);border-radius:4px;display:flex;align-items:center;justify-content:center}

/* nav */
.main-nav{left:0;top:135px;width:1200px;height:75px;background:var(--white);border-bottom:1px solid var(--grey)}
.main-nav ul{list-style:none;display:flex;position:absolute;left:124px;top:0;height:75px}
.main-nav li{display:flex;align-items:center;padding:0 21px;font-size:14px;color:var(--text)}
.main-nav li.active{background:var(--orange);color:var(--white)}

/* hero */
.hero{left:0;top:210px;width:1200px;height:410px;background:linear-gradient(180deg,#7d8792 0%,#a9b0b6 35%,#b98c6c 55%,#7c6a5c 78%,#d6d2cc 100%)}
.hero-caption{left:125px;top:340px;width:580px;height:122px;background:rgba(245,165,29,.72);padding:22px 30px;color:var(--white);font-size:26px;line-height:1.55}
.btn-dark{background:var(--ink);color:var(--orange);font-size:12px;letter-spacing:.5px;display:flex;align-items:center;justify-content:center}
.hero-btn{left:125px;top:505px;width:140px;height:50px;border-radius:4px;color:#f3c77a}
.hero-arrow{top:380px;width:44px;height:70px;background:var(--orange);display:flex;align-items:center;justify-content:center}

/* products */
.product-img{width:384px;height:171px}
.product-text{width:210px}
.product-text h3{font-weight:500;font-size:18px;color:var(--text);margin-bottom:8px}
.product-text p{font-size:11.5px;line-height:1.75;color:#333}
.product-text .btn-dark{width:137px;height:42px;margin-top:18px}
.left-text{left:532px}
.right-text{left:460px;text-align:right}
.right-text .btn-dark{margin-left:auto}
.coming{background:var(--orange)}

/* band */
.intro-band{left:0;top:1879px;width:1200px;height:255px;background:var(--ink)}
.intro-band p{position:absolute;left:150px;top:48px;width:900px;text-align:center;color:var(--orange);font-size:14px;line-height:1.5}
.btn-outline-orange{left:517px;top:2033px;width:165px;height:50px;border:2px solid var(--orange);border-radius:4px;color:var(--orange);font-size:13px;display:flex;align-items:center;justify-content:center}

/* video */
.video-card{left:124px;top:2158px;width:463px;height:340px;background:var(--orange);border-radius:14px}
.video-screen{left:150px;top:2195px;width:415px;height:225px;background:var(--white)}
.video-bar{left:150px;top:2420px;width:415px;height:16px;background:#111}
.video-caption{left:150px;top:2455px;font-size:14px;color:var(--ink)}
.systems h2{font-weight:500;font-size:25px;color:var(--ink);margin-bottom:18px}
.systems p{font-size:11.5px;line-height:1.65;color:#333;margin-bottom:16px}
.btn-outline-dark{left:612px;top:2389px;width:152px;height:46px;border:2px solid var(--ink);border-radius:4px;font-size:12px;display:flex;align-items:center;justify-content:center}

/* testimonial */
.testimonial{left:0;top:2545px;width:1200px;height:388px;background:var(--ink)}
.photo-ring{left:118px;top:2570px;width:330px;height:330px;border-radius:50%;background:var(--orange)}
.photo{left:140px;top:2592px;width:286px;height:286px;border-radius:50%;background:linear-gradient(180deg,#9fb3c4 0%,#b98c5c 50%,#6e6a62 100%)}
.bubble{left:430px;top:2620px;width:645px;height:235px;background:var(--orange);border-radius:10px;padding:22px 20px 0 18px;color:var(--ink)}
.bubble h3{font-weight:500;font-size:17px;margin-bottom:14px;padding-left:14px;white-space:nowrap}
.bubble p{font-size:11.5px;line-height:1.8;margin-bottom:14px}
.quote-author{right:124px;top:2857px;text-align:right;color:var(--orange);font-size:17px;line-height:1.45}

/* footer */
.site-footer{left:0;top:2933px;width:1200px;height:428px;background:var(--orange)}
.footer-col h4{font-size:13px;font-weight:700;color:var(--ink);padding-bottom:5px;border-bottom:1px solid var(--ink);margin-bottom:12px;display:inline-block;white-space:nowrap}
.footer-col ul{list-style:none}
.footer-col li{font-size:12px;line-height:30px;color:var(--ink)}
.footer-col p{font-size:12px;line-height:1.65;color:var(--ink)}
.col-divider{top:2990px;width:1px;height:230px;background:rgba(0,0,0,.15)}
.badge{width:62px;height:62px;background:var(--white);border-radius:8px}
.social{width:58px;height:58px;background:var(--ink);border-radius:8px}
.footer-phone{left:124px;top:3252px;font-size:12px;color:var(--ink)}
</style>
</head>
<body>

<header class="site-header abs">
  <div class="brand abs"><span class="brand-dot"></span>Kerbline Safety</div>
  <div class="tagline abs">Innovative edge protection system for the building industry - NZ wide</div>
  <div class="phone abs">800 KERBLN | 0800 537 256
    <span class="phone-icon"><svg width="16" height="16" viewBox="0 0 24 24"><path fill="#1a1512" d="M6.6 10.8a15.1 15.1 0 0 0 6.6 6.6l2.2-2.2c.3-.3.7-.4 1-.2 1.1.4 2.3.6 3.6.6.6 0 1 .4 1 1V20c0 .6-.4 1-1 1A17 17 0 0 1 3 4c0-.6.4-1 1-1h3.5c.6 0 1 .4 1 1 0 1.3.2 2.5.6 3.6.1.3 0 .7-.2 1z"/></svg></span>
  </div>
</header>

<nav class="main-nav abs">
  <ul>
    <li class="active">Home</li><li>About Us</li><li>Edge Protection Systems</li><li>Safety</li><li>Testimonials</li><li>Gallery</li><li>Downloads/Videos</li><li>Quote / Contact</li>
  </ul>
</nav>

<section class="hero abs" role="img" aria-label="Photo of a new house frame with roof trusses fitted with orange edge protection rails"></section>
<div class="hero-caption abs">Edge Protection Systems For New Houses With Timber Or Aluminium Rails</div>
<div class="hero-btn btn-dark abs">LEARN MORE</div>
<div class="hero-arrow abs" style="left:30px"><svg width="16" height="22"><path d="M14 2 3 11l11 9z" fill="#1a1512"/></svg></div>
<div class="hero-arrow abs" style="left:1126px"><svg width="16" height="22"><path d="M2 2l11 9-11 9z" fill="#1a1512"/></svg></div>

<div class="product-img abs" style="left:124px;top:647px;background:linear-gradient(120deg,#6f8f5a,#e0b020 55%,#f0c63a)" role="img" aria-label="Photo of a yellow soffit mount bracket"></div>
<div class="product-text left-text abs" style="top:650px"><h3>New Build Soffit Mount</h3><p>Lorem Ipsum is simply dummy text of the printing and typesetting industry. Lorem Ipsum has been the industry's standard dummy text ever since</p><div class="btn-dark">READ MORE</div></div>

<div class="product-text right-text abs" style="top:855px"><h3>New Build Truss Mount</h3><p>Lorem Ipsum is simply dummy text of the printing and typesetting industry. Lorem Ipsum has been the industry's standard dummy text ever since</p><div class="btn-dark">READ MORE</div></div>
<div class="product-img abs" style="left:694px;top:855px;background:linear-gradient(120deg,#d8dde2,#7a4a3a 50%,#e0b030)" role="img" aria-label="Photo of a yellow truss mount bracket on timber"></div>

<div class="product-img abs" style="left:124px;top:1060px;background:linear-gradient(180deg,#3d6fc0 0%,#8fb0d8 45%,#e9e9e6 70%,#5d7a4a 100%)" role="img" aria-label="Photo of a re-roof with edge protection rails"></div>
<div class="product-text left-text abs" style="top:1060px"><h3>Re-roof</h3><p>Lorem Ipsum is simply dummy text of the printing and typesetting industry. Lorem Ipsum has been the industry's standard dummy text ever since</p><div class="btn-dark">READ MORE</div></div>

<div class="product-text right-text abs" style="top:1265px"><h3>Garage and Sheds</h3><p>Lorem Ipsum is simply dummy text of the printing and typesetting industry. Lorem Ipsum has been the industry's standard dummy text ever since</p><div class="btn-dark">READ MORE</div></div>
<div class="product-img abs" style="left:694px;top:1266px;background:linear-gradient(120deg,#a7b8c6,#e2b02a 50%,#8a8f95)" role="img" aria-label="Photo of a yellow bracket on a garage roof"></div>

<div class="product-img coming abs" style="left:124px;top:1471px" role="img" aria-label="Coming soon hand lettering in white"></div>
<div class="product-text left-text abs" style="top:1471px"><h3>Commercial</h3><p>Lorem Ipsum is simply dummy text of the printing and typesetting industry. Lorem Ipsum has been the industry's standard dummy text ever since</p><div class="btn-dark">READ MORE</div></div>

<div class="product-text right-text abs" style="top:1676px"><h3>New Product</h3><p>Lorem Ipsum is simply dummy text of the printing and typesetting industry. Lorem Ipsum has been the industry's standard dummy text ever since</p><div class="btn-dark">READ MORE</div></div>
<div class="product-img coming abs" style="left:694px;top:1676px" role="img" aria-label="Coming soon hand lettering in white"></div>

<section class="intro-band abs">
  <p>Lorem Ipsum is simply dummy text of the printing and typesetting industry. Lorem Ipsum has been the industry's standard dummy text ever since the 1500s, when an unknown printer took a galley of type and scrambled it to make a type specimen book. It has survived not only five centuries, but also the leap into electronic typesetting, remaining essentially unchanged. It was popularised in the 1960s with the release of Letraset sheets containing</p>
</section>
<div class="btn-outline-orange abs">READ MORE</div>

<div class="video-card abs"></div>
<div class="video-screen abs" role="img" aria-label="Video still of a yellow edge protection bracket"></div>
<svg class="abs" style="left:287px;top:2245px" width="140" height="140" viewBox="0 0 140 140"><circle cx="70" cy="70" r="70" fill="#d9d9d9" opacity=".9"/><path d="M55 42l40 28-40 28z" fill="#111"/></svg>
<div class="video-bar abs"></div>
<div class="video-caption abs">Watch the video on how the Edge Protection system works</div>

<div class="systems abs" style="left:612px;top:2180px;width:455px">
  <h2>Edge Protection Systems...</h2>
  <p>Edge Protection is essential when working on buildings at height. Our systems are designed by experienced tradesmen and are manufactured in New Zealand.</p>
  <p>The K Bracket is without a doubt the most versatile and cost effective Edge Protection on the market. The K Bracket system has been designed (and has passed stringent testing) to comply with AS/NZS 3993:2009.</p>
</div>
<div class="btn-outline-dark abs">READ MORE</div>

<section class="testimonial abs"></section>
<div class="photo-ring abs"></div>
<div class="photo abs" role="img" aria-label="Photo of builders standing in front of a house frame with edge protection"></div>
<div class="bubble abs">
  <h3>"I Would Recommend Kerbline Safety NZ Ltd. To Any Prospective Purchaser"</h3>
  <p>Marlow Homes Ltd. has used the services of Tom Reddale and his Edge Protection. I was impressed both with the quality of the Edge Protection Tom Supplied and his knowledge and understanding of the new requirements being enforced by the Labour Dept.</p>
  <p>I had a meeting with the Labour Dept. representative in my office which Tom attended and Tom introduced a simple and easy way to address the issue which was more than the Labour Dept. were prepared to offer</p>
</div>
<div class="quote-author abs">Joanne Pryor,<br>Director of Marlow Homes Ltd</div>

<footer class="site-footer abs"></footer>
<div class="footer-col abs" style="left:124px;top:2978px">
  <h4>Quick Link</h4>
  <ul><li>Home</li><li>About Us</li><li>Safety</li><li>Testimonials</li><li>Gallery</li><li>Downloads/Videos</li><li>Quote / Contact</li></ul>
</div>
<div class="col-divider abs" style="left:270px"></div>
<div class="footer-col abs" style="left:287px;top:2978px">
  <h4>Edge Protection Systems</h4>
  <ul><li>-- New Build Soffit Mount</li><li>-- New Build Truss Mount</li><li>-- Re-roof</li><li>-- Garage and Sheds</li><li>-- Commercial</li><li>--coming soon</li><li>-- New product – coming soon</li></ul>
</div>
<div class="col-divider abs" style="left:515px"></div>
<div class="footer-col abs" style="left:530px;top:2978px;width:300px">
  <h4>Patent. 718305 Design Registration.429862</h4>
  <p>Important. All our systems are the property of Kerbline Safety New Zealand Ltd. It is company policy to vigorously prosecute any attempts to copy our innovations and designs.</p>
</div>
<div class="col-divider abs" style="left:840px"></div>
<div class="footer-col abs" style="left:857px;top:2978px;width:220px">
  <h4>Proudly New Zealand Made</h4>
</div>
<div class="badge abs" style="left:857px;top:3020px"></div>
<div class="social abs" style="left:983px;top:3020px"></div>
<div class="abs" style="left:948px;top:3084px;font-size:12px;color:var(--ink)">www.kerblinesafety.social</div>
<div class="footer-phone abs">0800 KERBLN | 0800 537 256</div>

</body>
</html>
```